Tamsworth Counsel Cover 3 - Capital Allocation battlefield

Tamsworth Counsel is a business consulting firm. We will publish a series of four thought leadership pieces online and via PDF. The third of the series is attached to this project. We need an eye-catching cover page with a back page that keeps with our branding. The document attached is in the final draft, and the cover and pack pages are placeholders only. You can find more about our branding and style on our website www.tamsworthcounsel.com.au. The other three projects can be found here with a similar brief, and you are welcome to submit a design for all 4.

```html
<!DOCTYPE html>
<html lang="en">
<head>
<meta charset="utf-8">
<title>Tamsworth Counsel – The Capital Allocation battlefield</title>
<link href="https://fonts.googleapis.com/css2?family=Catamaran:wght@300;400;600;700;800&display=swap" rel="stylesheet">
<style>
  :root {
    --stage: #636363;
    --paper: #ffffff;
    --blue: #00aeef;
    --orange: #f7941d;
    --ink: #111111;
    --art-light: #fde3c2;
    --art-mid: #f9b668;
  }
  * { margin: 0; padding: 0; box-sizing: border-box; }
  html, body { width: 1200px; height: 870px; overflow: hidden; background: var(--stage); }
  body { position: relative; font-family: "Catamaran", sans-serif; color: var(--ink); }

  .page { position: absolute; top: 70px; width: 520px; height: 736px; background: var(--paper); overflow: hidden; }
  .page--cover { left: 57px; }
  .page--back { left: 611px; }

  .brand { position: absolute; display: flex; align-items: center; gap: 10px; }
  .brand__dot { border-radius: 50%; background: var(--orange); flex: none; }
  .brand__name { color: var(--blue); font-weight: 700; line-height: 0.95; }
  .page--cover .brand { left: 35px; top: 37px; }
  .page--cover .brand__dot { width: 40px; height: 40px; }
  .page--cover .brand__name { font-size: 21px; }
  .page--back .brand { left: 150px; top: 62px; }
  .page--back .brand__dot { width: 56px; height: 56px; }
  .page--back .brand__name { font-size: 28px; }

  .triangles { position: absolute; }

  .city-art { position: absolute; background: linear-gradient(180deg, var(--art-mid) 0%, var(--art-light) 70%, rgba(253,227,194,0) 100%); }
  .page--cover .city-art { left: 28px; top: 317px; width: 465px; height: 364px; }
  .page--back .city-art { left: 362px; top: 160px; width: 142px; height: 330px; }

  .cover-title { position: absolute; left: 35px; top: 134px; color: var(--blue); font-weight: 800; font-size: 40px; line-height: 42px; letter-spacing: -0.3px; }
  .cover-subtitle { position: absolute; left: 35px; top: 272px; display: flex; align-items: center; gap: 8px; font-size: 19px; font-weight: 400; }
  .cover-subtitle__mark { width: 21px; height: 13px; background: var(--orange); }

  .cover-footer__rule { position: absolute; left: 23px; top: 700px; width: 270px; height: 1.5px; background: var(--orange); }
  .cover-footer__url { position: absolute; right: 23px; top: 689px; color: var(--blue); font-size: 14px; white-space: nowrap; }

  .contact-call { position: absolute; left: 45px; top: 200px; width: 310px; font-size: 14px; line-height: 20px; text-transform: uppercase; font-weight: 400; }
  .contact-call strong { color: var(--orange); font-weight: 700; }
  .contact-call__rule { position: absolute; left: 45px; top: 266px; width: 35px; height: 3px; background: var(--orange); }

  .person { position: absolute; left: 45px; width: 240px; }
  .person--first { top: 296px; }
  .person--second { top: 374px; left: 48px; }
  .person__name { font-size: 16px; font-weight: 700; line-height: 20px; }
  .person__role { color: var(--orange); font-size: 10.5px; line-height: 14px; margin-bottom: 4px; }
  .person__line { color: var(--blue); font-size: 10px; line-height: 13px; }
  .person__line b { font-weight: 700; }

  .follow { position: absolute; left: 48px; top: 577px; display: flex; align-items: center; gap: 3px; color: var(--orange); font-size: 16px; }
  .follow__icon { width: 16px; height: 16px; border-radius: 50%; background: var(--blue); }
  .follow__icon--dark { background: var(--ink); }
  .follow__text { margin-right: 3px; }
  .back-url { position: absolute; left: 48px; top: 597px; color: var(--orange); font-weight: 700; font-size: 14px; }
</style>
</head>
<body>

<section class="page page--cover">
  <div class="brand">
    <span class="brand__dot"></span>
    <span class="brand__name">Tamsworth<br>Counsel</span>
  </div>

  <svg class="triangles" style="left:330px;top:97px" width="175" height="202" viewBox="0 0 175 202" aria-hidden="true">
    <polygon points="0,100 175,0 175,202" fill="var(--blue)"/>
    <polygon points="23,69 82,36 82,103" fill="var(--orange)"/>
  </svg>

  <h1 class="cover-title">The Capital<br>Allocation<br>battlefield</h1>
  <p class="cover-subtitle"><span class="cover-subtitle__mark"></span>Deploying the war chest</p>

  <div class="city-art" role="img" aria-label="Orange city skyline of office towers built from window blocks"></div>

  <div class="cover-footer__rule"></div>
  <p class="cover-footer__url">www.tamsworthcounsel.com.au</p>
</section>

<section class="page page--back">
  <div class="brand">
    <span class="brand__dot"></span>
    <span class="brand__name">Tamsworth<br>Counsel</span>
  </div>

  <div class="city-art" role="img" aria-label="Orange city skyline of office towers built from window blocks"></div>

  <p class="contact-call">Contact us to find out how Tamsworth Counsel can help build your company into a market <strong>leader today.</strong></p>
  <div class="contact-call__rule"></div>

  <div class="person person--first">
    <p class="person__name">Hugh Tamsworth</p>
    <p class="person__role">Managing Director</p>
    <p class="person__line"><b>Mobile</b> +61 400 318 226</p>
    <p class="person__line"><b>Email</b> hugh@tamsworthcounsel.com.au</p>
  </div>

  <div class="person person--second">
    <p class="person__name">Owen Tamsworth</p>
    <p class="person__role">Managing Director</p>
    <p class="person__line"><b>Mobile</b> +61 400 964 571</p>
    <p class="person__line"><b>Email</b> owen@tamsworthcounsel.com.au</p>
  </div>

  <svg class="triangles" style="left:330px;top:487px" width="175" height="203" viewBox="0 0 175 203" aria-hidden="true">
    <polygon points="0,102 175,0 175,203" fill="var(--blue)"/>
    <polygon points="23,70 82,36 82,105" fill="var(--orange)"/>
  </svg>

  <p class="follow"><span class="follow__text">Follow</span><span class="follow__icon"></span><span class="follow__icon follow__icon--dark"></span></p>
  <p class="back-url">tamsworthcounsel.com.au</p>
</section>

</body>
</html>
```